Flyer für Pflegeeinrichtung
Zielgruppe
Wir sind eine Pflegeeinrichtung. Unser ambulanter Pflegedienst aus Lindhagen zieht am 01.07.2024 nach Lindhagen Zentrum. Diesen Umzug möchte ich gerne mit Flyern bewerben.
Aufgabenstellung
Ich dachte an DIN Lang Flyer. Gerne auffällige Farben die ins Auge stechen bzw schöne Lontraste haben. Die Zielgruppe sind Senioren sowie auch deren Angehörige. Also zwischen 20-99 Jahre. Es sollte der Umzug selbst, die Neueröffnung sowie eine Art Einladung zu diesem Tag vorhanden sein. Auch das wir als ambulanter Pflegedienst Grundpflege, Hauswirtschaft ärztlich verordnete Leistungen durchführen. In Lindhagen am 'alten Standort' haben wir auch unsere Tagespflege. Vielleicht bekommt man diese noch geschickt dazwischen.

```html
<!DOCTYPE html>
<html lang="de">
<head>
<meta charset="utf-8">
<title>Haus Seeblick – Einladung zur Neueröffnung</title>
<link href="https://fonts.googleapis.com/css2?family=Open+Sans:wght@400;600;700&display=swap" rel="stylesheet">
<style>
  :root{
    --bg:#ece9e2;
    --paper:#f4f4f4;
    --white:#ffffff;
    --red:#c93330;
    --red-dark:#b22a28;
    --teal:#3ea8a2;
    --ink:#2b2b2b;
    --ink-soft:#4a4a4a;
    --navy:#1f3d6b;
  }
  *{box-sizing:border-box;margin:0;padding:0}
  html,body{width:1200px;height:800px;overflow:hidden}
  body{background:var(--bg);font-family:"Open Sans",sans-serif;color:var(--ink)}
  .flyer{position:absolute;left:60px;top:114px;width:1080px;height:572px;display:flex;box-shadow:0 18px 40px rgba(0,0,0,.18)}
  .panel{position:relative;width:270px;height:572px;background:var(--paper);overflow:hidden}
  .panel + .panel{border-left:1px solid #e2e2e2}

  /* cover */
  .cover{background:var(--white)}
  .brand{height:150px;display:flex;flex-direction:column;align-items:center;justify-content:center;gap:4px}
  .brand-name{font-size:24px;font-weight:700;color:var(--navy);display:flex;align-items:center;gap:8px}
  .brand-dot{width:12px;height:12px;border-radius:50%;background:var(--red)}
  .brand-tag{font-size:12px;font-weight:600;color:var(--navy);letter-spacing:.5px}
  .cover-photo{position:absolute;left:0;top:150px;width:270px;height:422px;
    background:linear-gradient(180deg,#8fb6d8 0%,#dfe6ea 30%,#cfd3d6 60%,#9c9a96 100%)}
  .cover-band{position:absolute;left:0;bottom:0;width:270px;height:230px}
  .cover-text{position:absolute;left:34px;bottom:40px;color:var(--white)}
  .cover-text h1{font-size:26px;font-weight:700;line-height:1.1;margin-bottom:6px}
  .cover-text p{font-size:14px;font-weight:600;line-height:1.3}

  /* photos */
  .photo{position:absolute}
  .photo-family{left:18px;top:16px;width:140px;height:110px;border-radius:0 0 46px 46px;
    background:linear-gradient(135deg,#efe7df,#c9b6a6 60%,#8d7a6c)}
  .photo-meal{left:150px;top:0;width:120px;height:100px;border-radius:0 0 0 50px;
    background:linear-gradient(135deg,#e8dcd0,#e7b46a 50%,#b8c79a)}
  .photo-table{left:0;bottom:0;width:270px;height:220px;border-radius:90px 0 0 0;
    background:linear-gradient(160deg,#f2efec,#d9cfc7 45%,#a84a47 85%)}
  .photo-group{left:0;top:0;width:270px;height:200px;border-radius:0 0 110px 0;
    background:linear-gradient(160deg,#f1eeea,#9a9087 45%,#5a524c)}
  .photo-house{left:12px;bottom:40px;width:258px;height:210px;border-radius:40px 60px 0 0;
    background:linear-gradient(180deg,#7fa9d6 0%,#c9dcec 35%,#ecebe8 55%,#b9b2aa 100%)}

  /* inside text */
  .copy{position:absolute;left:24px;right:22px}
  .headline{font-size:14px;font-weight:700;line-height:1.25;color:var(--ink);padding-bottom:6px;border-bottom:2px solid var(--teal);margin-bottom:12px}
  .copy p{font-size:10.5px;line-height:1.5;color:var(--ink-soft);margin-bottom:9px}
  .service .copy{top:170px}
  .invite .copy{top:222px}
  .daycare .copy{top:110px}
</style>
</head>
<body>
<main class="flyer">

  <section class="panel cover">
    <div class="brand">
      <div class="brand-name"><span class="brand-dot"></span>Haus Seeblick</div>
      <div class="brand-tag">Pflege am Meer</div>
    </div>
    <div class="cover-photo" role="img" aria-label="Foto: weißes Gebäude des Pflegedienstes mit Dienstwagen davor"></div>
    <svg class="cover-band" viewBox="0 0 270 230" aria-hidden="true">
      <path d="M0 230 L0 150 C10 60 120 30 270 0 L270 230 Z" fill="var(--red)"/>
    </svg>
    <div class="cover-text">
      <h1>Einladung</h1>
      <p>zur Neueröffnung<br>unseres ambulanten<br>Pflegedienstes</p>
    </div>
  </section>

  <section class="panel service">
    <div class="photo photo-family" role="img" aria-label="Foto: Familie mit Kleinkind und Seniorin beim Brettspiel"></div>
    <div class="photo photo-meal" role="img" aria-label="Foto: Teller mit Salat und Mittagessen"></div>
    <div class="copy">
      <h2 class="headline">Neuer Standort -<br>gleicher Service</h2>
      <p>Auch in unseren neuen Räumlichkeiten können Sie weiterhin auf unsere Unterstützung zählen.</p>
      <p>Bei uns finden Sie unter anderem Grundpflege, umfassende Hauswirtschaft und wir führen auch ärztlich verordnete Leistungen durch.</p>
    </div>
    <div class="photo photo-table" role="img" aria-label="Foto: Pflegerin mit Seniorinnen am gedeckten Tisch"></div>
  </section>

  <section class="panel invite">
    <div class="photo photo-group" role="img" aria-label="Foto: Pflegerin mit zwei Senioren in heller Stube"></div>
    <div class="copy">
      <h2 class="headline">Wir ziehen um und Sie<br>sind herzlich eingeladen!</h2>
      <p>Unser ambulanter Pflegedienst aus Lindhagen zieht am 01.07.2024 nach Lindhagen Zentrum.</p>
      <p>Wir hätten Sie gerne dabei, unsere neuen Räumlichkeiten einzuweihen.</p>
      <p>Wir freuen uns auf Sie.</p>
    </div>
  </section>

  <section class="panel daycare">
    <div class="copy">
      <h2 class="headline">Tagespflege<br>am "alten" Standort</h2>
      <p>Auch wenn wir einen neuen Standort eröffnen, verbleibt unser vorheriger Standort in Lindhagen als Tagespflege, wo wir weiterhin für Sie da sein werden.</p>
    </div>
    <div class="photo photo-house" role="img" aria-label="Foto: weißes Haus mit rotem Dach, Standort der Tagespflege"></div>
  </section>

</main>
</body>
</html>
```